ruCover Business Card Design Project

We need a business card design for ruCover. ruCover is an underwriting agency. Underwriting agencies act on behalf of insurers, to underwrite insurance. We will be operating in specialised classes of insurance initially and looking to expand from there. We would like to see designs that incorporate our logo colours as well as a contrasting stand out colour - also we'd like the logo itself to be embossed on the card.

Insurance

Requirements
Must have
• Logo on front
Nice to have
• Logo solely featured on back of card
Should not have
• Please do not use comic cans font :)

```html
<!DOCTYPE html>
<html lang="en">
<head>
<meta charset="utf-8">
<title>ruCover Business Cards</title>
<link href="https://fonts.googleapis.com/css2?family=Arimo:wght@400;700&display=swap" rel="stylesheet">
<style>
  :root {
    --backdrop: #3d4044;
    --card: #ffffff;
    --ink-dark: #3b3d42;
    --ink-blue: #1f5fa8;
    --ink-grey: #6d6f73;
    --ink-soft: #8a8c90;
  }
  * { margin: 0; padding: 0; box-sizing: border-box; }
  html, body {
    width: 1200px;
    height: 900px;
    overflow: hidden;
    background: var(--backdrop);
    font-family: "Arimo", Arial, sans-serif;
  }
  .canvas {
    position: relative;
    width: 1200px;
    height: 900px;
  }
  .card {
    position: absolute;
    background: var(--card);
  }
  .card--front {
    left: 30px;
    top: 30px;
    width: 720px;
    height: 400px;
    display: flex;
    align-items: center;
    justify-content: center;
  }
  .card--back {
    left: 460px;
    top: 450px;
    width: 710px;
    height: 420px;
  }
  .brand {
    display: flex;
    flex-direction: column;
    align-items: center;
    gap: 12px;
  }
  .brand__dot {
    width: 110px;
    height: 110px;
    border-radius: 50%;
    background: var(--ink-blue);
  }
  .brand__name {
    font-weight: 700;
    font-size: 78px;
    letter-spacing: -1px;
    color: var(--ink-blue);
    line-height: 1;
  }
  .holder {
    position: absolute;
    left: 150px;
    top: 70px;
    display: inline-flex;
    flex-direction: column;
    align-items: flex-end;
  }
  .holder__name {
    font-weight: 700;
    font-size: 66px;
    letter-spacing: -1px;
    line-height: 1;
  }
  .holder__first { color: var(--ink-dark); }
  .holder__last { color: var(--ink-blue); }
  .holder__role {
    margin-top: 6px;
    font-weight: 700;
    font-size: 20px;
    color: var(--ink-soft);
  }
  .contact {
    position: absolute;
    left: 150px;
    top: 220px;
    list-style: none;
    font-size: 22px;
    line-height: 30px;
  }
  .contact__row--email { margin-top: 24px; }
  .contact__label {
    font-weight: 700;
    color: var(--ink-dark);
  }
  .contact__value {
    font-weight: 700;
    color: var(--ink-soft);
  }
</style>
</head>
<body>
<main class="canvas">
  <section class="card card--front" aria-label="Card front">
    <div class="brand">
      <span class="brand__dot" aria-hidden="true"></span>
      <span class="brand__name">ruCover</span>
    </div>
  </section>

  <section class="card card--back" aria-label="Card back">
    <div class="holder">
      <h1 class="holder__name"><span class="holder__first">dan</span><span class="holder__last">Kestrow</span></h1>
      <p class="holder__role">Managing Director</p>
    </div>
    <ul class="contact">
      <li class="contact__row"><span class="contact__label">Mobile:</span> <span class="contact__value">XXXXXX XXXXX</span></li>
      <li class="contact__row"><span class="contact__label">Work:</span> <span class="contact__value">XXXXXX XXXXX ex.XXX</span></li>
      <li class="contact__row contact__row--email"><span class="contact__label">Email:</span> <span class="contact__value">XXXXXX@XXXXXXXXXXX</span></li>
    </ul>
  </section>
</main>
</body>
</html>
```